Data company needs a Website designed, coded and published.

We are a startup data company that needs to build a professional website.
Our business, Quillbrook Analytics, provides PII data to large national advertisers so they can precisely target Real People who are their consumers with advertising messages.

As a startup in this space, our website must establish our credibility and position us against significantly larger and more established competitors. Because we are in a data and technology space, it is vital for this slight to be incredibly slick and professional. Additionally, the purpose of the site is to inform potential customers about the quality of our data, the safety and security measures we take, should provide insight on how a prospect could engage us and ultimately the site should capture potential leads for us.

We have provided the attached presentation deck that is intended to give you an idea of the kind of content we'd like to have on the site. This deck is not intended to restrict your creativity in how the site should look and what it should say. It's simply intended to give you an outline of what we want to say.

We are open to your creative and alternative approaches.

Industry/Entity Type

Technology, Data, Media

Coding

Coded - Design and coding required

Number of Pages Required

5+ page

Font styles to use
Sans Serif

Colors

Designer to choose colors to be used in the design.

Requirements
Must have
• Professional looking site that positions us among the very best in our industry.
Nice to have
• We are about targeting real people with media and so we want to have good clean images of REAL People throughout the site.

```html
<!DOCTYPE html>
<html lang="en">
<head>
<meta charset="utf-8">
<title>Quillbrook Analytics — PII Data for Precise Targeting</title>
<link href="https://fonts.googleapis.com/css2?family=Kanit:wght@300;400;500;700;800&display=swap" rel="stylesheet">
<style>
:root{
  --blue:#0a63e6;
  --blue-bright:#1a8cff;
  --cyan:#12c8f5;
  --navy:#0b1640;
  --navy-deep:#0a1233;
  --ink:#111111;
  --text:#2b2b2b;
  --gray:#ececef;
  --white:#ffffff;
}
*{margin:0;padding:0;box-sizing:border-box}
html,body{width:1200px;height:3429px;overflow:hidden}
body{position:relative;font-family:"Kanit",sans-serif;color:var(--text);background:var(--white)}
.abs{position:absolute}
h1,h2,h3{font-family:"Kanit",sans-serif;font-weight:800;color:var(--ink);letter-spacing:.2px}
.btn{position:absolute;display:flex;align-items:center;justify-content:center;background:var(--blue);color:var(--white);font-size:13px;font-weight:500;text-transform:uppercase;border-radius:3px;text-decoration:none}

/* hero */
.hero{left:0;top:0;width:1200px;height:665px;background:linear-gradient(100deg,#f4f6f8 0%,#e9edf1 40%,#cfd8e2 70%,#aebccb 100%)}
.hero-photo{left:440px;top:0;width:760px;height:665px;background:linear-gradient(90deg,rgba(233,237,241,0) 0%,#c9d3dd 35%,#9fb0c2 75%,#7d8fa3 100%)}
.logo{left:43px;top:64px;display:flex;align-items:center;gap:10px}
.logo-mark{width:22px;height:22px;background:var(--blue);border-radius:3px}
.logo-name{font-size:26px;font-weight:700;color:var(--ink)}
.nav{top:64px;right:43px;display:flex;gap:21px;font-size:13.5px;color:var(--ink)}
.hero h1{left:40px;top:280px;font-size:57px;line-height:70px}
.hero p{left:43px;top:448px;width:420px;font-size:13.5px;line-height:24px;color:var(--ink)}

/* bands */
.band{left:0;width:1200px}

/* audience */
.audience{left:0;top:690px;width:1200px;height:476px;background:var(--gray)}
.audience-photo{left:692px;top:690px;width:508px;height:476px;background:linear-gradient(110deg,#3a4a6a 0%,#1e3a7a 40%,#14306b 70%,#0c2357 100%)}
.audience h2{left:43px;top:808px;font-size:38px;line-height:52px}
.audience p{left:43px;top:928px;width:520px;font-size:13.5px;line-height:24px;color:var(--ink)}

/* data */
.data{left:0;top:1166px;width:1200px;height:624px;background:linear-gradient(100deg,#0b1640 0%,#0f1f52 45%,#17306e 75%,#1d3d80 100%)}
.data h2{left:42px;top:1308px;font-size:38px;line-height:52px;color:var(--white)}
.bullets{left:43px;top:1424px;width:490px;list-style:none;color:var(--white);font-size:13.5px;line-height:23px}
.bullets li{position:relative;padding-left:22px;margin-bottom:7px}
.bullets li::before{content:"";position:absolute;left:0;top:6px;width:12px;height:12px;border-radius:50%;background:var(--blue-bright)}

/* channels */
.channels h2{left:0;top:1826px;width:1200px;text-align:center;font-size:38px;line-height:51px}
.channels .sub{left:0;top:1998px;width:1200px;text-align:center;font-size:23px;font-weight:300;color:var(--ink)}
.chan{position:absolute;width:120px;text-align:center;font-size:16px;color:var(--ink)}
.chan svg{display:block;margin:0 auto 10px}

/* attribution */
.attr-art{left:30px;top:2440px;width:590px;height:500px;background:radial-gradient(ellipse at 45% 50%,#6c9fe0 0%,#a9c6ea 35%,#e6eef8 65%,#ffffff 85%)}
.attr h2{left:701px;top:2440px;font-size:37px}
.attr p{left:701px;width:470px;font-size:13.5px;line-height:24px;color:var(--ink)}
.attr .list{left:701px;top:2606px;width:470px;list-style:none;font-size:13.5px;line-height:24px;color:var(--ink)}
.attr .list li{position:relative;padding-left:22px;margin-bottom:6px}
.attr .list li::before{content:"";position:absolute;left:0;top:6px;width:12px;height:12px;border-radius:50%;background:var(--blue-bright)}
.feat{left:697px;width:300px;display:flex;align-items:center;gap:10px;font-size:13.5px;color:var(--ink)}
.feat i{display:block;width:17px;height:17px;border:2px solid var(--blue-bright);border-radius:4px;background:#d8ecff}

/* footer */
.footer{left:0;top:3181px;width:1200px;height:248px;background:var(--navy-deep)}
.foot-nav{left:0;top:3232px;width:1200px;display:flex;justify-content:center;gap:20px;font-size:13.5px;color:var(--white)}
.socials{left:0;top:3294px;width:1200px;display:flex;justify-content:center;gap:39px}
.socials span{width:39px;height:39px;border-radius:50%;background:var(--blue-bright)}
.copy{left:0;top:3400px;width:1200px;text-align:center;font-size:11px;color:var(--white)}
</style>
</head>
<body>

<section class="hero abs">
</section>
<div class="hero-photo abs" role="img" aria-label="Shopping mall scene with a digital signage screen showing a personalized offer and a shopper being recognized"></div>
<div class="logo abs"><span class="logo-mark"></span><span class="logo-name">Quillbrook Analytics</span></div>
<nav class="nav abs"><span>Our Data</span><span>Solutions</span><span>Why Quillbrook?</span><span>Careers</span><span>Contact Us</span><span>About Us</span></nav>
<div class="hero">
  <h1 class="abs">PII Data for<br>Precise Targeting</h1>
  <p class="abs">Ethically and intelligently target REAL PEOPLE with your programmatic media. No Cookies. No Bots.</p>
</div>
<a class="btn" style="left:43px;top:516px;width:193px;height:46px">Schedule a demo</a>

<svg class="band abs" style="top:665px" width="1200" height="62" viewBox="0 0 1200 62" aria-hidden="true">
  <polygon points="0,0 1200,0 1200,62 0,30" fill="#0a5de0"/>
  <polygon points="700,0 1200,0 1200,62" fill="#12c8f5"/>
</svg>

<section class="audience abs"></section>
<div class="audience-photo abs" role="img" aria-label="Person in glasses looking at a digital globe surrounded by portraits of real people"></div>
<svg class="band abs" style="top:665px" width="1200" height="62" viewBox="0 0 1200 62" aria-hidden="true">
  <polygon points="0,0 1200,0 1200,62 0,30" fill="#0a5de0"/>
  <polygon points="700,0 1200,0 1200,62" fill="#12c8f5"/>
</svg>
<div class="audience">
  <h2 class="abs">Identify the Right Audience<br>and Fill the Top of The Funnel</h2>
  <p class="abs">Quillbrook Analytics allows you to identify the consumers who are just starting their journey...<br>And because we start with the names of Real People...<br>Quillbrook Analytics allows you to track and manage your communication and messaging throughout the entire journey.</p>
</div>
<a class="btn" style="left:43px;top:1067px;width:171px;height:38px">Learn more</a>

<section class="data abs" role="img" aria-label="Hands typing on a laptop with a holographic team organisation chart"></section>
<div class="data">
  <h2 class="abs">Precise People-Based Targeting<br>Starts with Our Data</h2>
  <ul class="bullets abs">
    <li>Cookie-Free PII Data on 160M Real People Connected to 700M+ Devices</li>
    <li>Precise Targeting to Real People (not inferred personas)</li>
    <li>Individualized Media Plans for Each Target Customer based on their Media Habits</li>
    <li>Complete Attribution Across Channels</li>
    <li>100% permission-based, opt-in and CCPA, GDPR &amp; CAN-SPAM compliant</li>
  </ul>
</div>
<a class="btn" style="left:43px;top:1633px;width:192px;height:37px">More about our data</a>

<section class="channels">
  <h2 class="abs">Serve Ads Only on Channels/<br>Devices Your Target is<br>Actually Using.</h2>
  <p class="sub abs">Use Quillbrook’s Data on these channels:</p>

  <div class="chan" style="left:315px;top:2060px">
    <svg width="70" height="52" viewBox="0 0 70 52"><rect x="2" y="2" width="66" height="48" rx="5" fill="#1a8cff"/><path d="M2 8 L35 30 L68 8" fill="none" stroke="#8fd0ff" stroke-width="3"/></svg>Email</div>
  <div class="chan" style="left:474px;top:2060px">
    <svg width="70" height="52" viewBox="0 0 70 52"><rect x="6" y="2" width="58" height="40" rx="4" fill="#1a8cff"/><rect x="12" y="8" width="46" height="28" fill="#8fd0ff"/><rect x="2" y="42" width="66" height="8" rx="3" fill="#0a63e6"/></svg>Display</div>
  <div class="chan" style="left:623px;top:2060px">
    <svg width="70" height="66" viewBox="0 0 70 66" style="margin-top:-14px"><rect x="14" y="2" width="42" height="62" rx="6" fill="#8fd0ff"/><rect x="28" y="2" width="14" height="4" rx="2" fill="#1a8cff"/></svg>Mobile</div>
  <div class="chan" style="left:765px;top:2060px">
    <svg width="70" height="66" viewBox="0 0 70 66" style="margin-top:-14px"><rect x="6" y="2" width="58" height="62" rx="5" fill="#8fd0ff"/><g stroke="#1a8cff" stroke-width="3"><line x1="20" y1="12" x2="20" y2="54"/><line x1="35" y1="12" x2="35" y2="54"/><line x1="50" y1="12" x2="50" y2="54"/></g><g fill="#1a8cff"><circle cx="20" cy="40" r="5"/><circle cx="35" cy="24" r="5"/><circle cx="50" cy="36" r="5"/></g></svg>Audio</div>

  <div class="chan" style="left:315px;top:2212px">
    <svg width="70" height="62" viewBox="0 0 70 62" style="margin-top:-10px"><circle cx="35" cy="31" r="30" fill="#1a8cff"/><polygon points="24,18 24,44 40,31" fill="#8fd0ff"/><polygon points="36,18 36,44 52,31" fill="#8fd0ff"/></svg>Video</div>
  <div class="chan" style="left:474px;top:2212px">
    <svg width="70" height="62" viewBox="0 0 70 62" style="margin-top:-10px"><rect x="2" y="2" width="66" height="46" rx="4" fill="#1a8cff"/><rect x="8" y="8" width="54" height="34" fill="#8fd0ff"/><rect x="28" y="48" width="14" height="8" fill="#0a63e6"/><rect x="18" y="56" width="34" height="4" rx="2" fill="#0a63e6"/></svg>TV</div>
  <div class="chan" style="left:623px;top:2212px">
    <svg width="70" height="62" viewBox="0 0 70 62" style="margin-top:-10px"><circle cx="35" cy="31" r="30" fill="#8fd0ff"/><g fill="#1a8cff"><circle cx="24" cy="31" r="6"/><circle cx="46" cy="19" r="6"/><circle cx="46" cy="43" r="6"/></g><path d="M24 31 L46 19 M24 31 L46 43" stroke="#1a8cff" stroke-width="3"/></svg>Social</div>
  <div class="chan" style="left:765px;top:2212px">
    <svg width="70" height="66" viewBox="0 0 70 66" style="margin-top:-14px"><polygon points="35,2 66,26 4,26" fill="#1a8cff"/><rect x="8" y="26" width="54" height="38" fill="#8fd0ff"/><rect x="28" y="40" width="16" height="24" fill="#1a8cff"/></svg>Direct Mail</div>
</section>

<section class="attr">
  <div class="attr-art abs" role="img" aria-label="Hexagon collage of people at work with phones, laptops, charts and ad layouts"></div>
  <h2 class="abs">Attribution</h2>
  <p class="abs" style="top:2498px">As a PII company Quillbrook can provide POINT OF SALE MATCHBACK. Providing a precise picture of the impact of your media. Regardless of how and where the target becomes your customer.</p>
  <p class="abs" style="top:2578px;font-style:italic">We identify:</p>
  <ul class="list abs">
    <li>Winning combination of channels and strategies drive conversions.</li>
    <li>What kind of improvements are possible. We scale down less effective tactics and serve up new tests.</li>
    <li>Campaigns get smarter, more effective and more efficiently over time.</li>
  </ul>
  <div class="feat abs" style="top:2754px"><i></i>Response Analysis</div>
  <div class="feat abs" style="top:2787px"><i></i>Cross-device Pixel Tracking</div>
  <div class="feat abs" style="top:2821px"><i></i>Point of Sale Matchback</div>
</section>
<a class="btn" style="left:696px;top:2874px;width:172px;height:37px">Schedule a demo</a>

<svg class="band abs" style="top:3126px" width="1200" height="56" viewBox="0 0 1200 56" aria-hidden="true">
  <polygon points="0,22 1200,0 1200,56 0,56" fill="#0a5de0"/>
  <polygon points="760,8 1200,0 1200,56 900,56" fill="#12c8f5"/>
</svg>
<footer class="footer abs"></footer>
<nav class="foot-nav abs"><span>Our Data</span><span>Solutions</span><span>Why Quillbrook?</span><span>Careers</span><span>Contact Us</span><span>About Us</span></nav>
<div class="socials abs" aria-label="Social links"><span></span><span></span><span></span><span></span></div>
<p class="copy abs">Quillbrook Analytics ©2023 &nbsp;All rights reserved.</p>

</body>
</html>
```